A Lantern on the pier.

I need a book cover (and back cover) design for a novel. The novel is a thiller. ´Synopsis: During the party after an awards ceremony at prestigious institution, one of the young awarders dissapear. The last place where he left a trace was close to a giant chessboard in the grass of the beautiful gardens of the place of ceremony. The detective in charge of finding the missing person and find out what happened will gradually discover that the institution is not all that it seems.
The book cover size will be 9" x 6" and the title of the novel "A lantern on the pier" will be name in spanish "Una linterna en el muelle". The back cover will have a synopsis (in spanish )that i will develop later on.
One suggestion for the design: I always love the art of MILO TRENT for movie posters, so I´m looking for something of similar style, you know (the girl who sold paper kites, North pier ballad, halvorn, ledger of shadows, etc

```html
<!DOCTYPE html>
<html lang="es">
<head>
<meta charset="utf-8">
<title>Una linterna en el muelle — cubierta</title>
<link rel="stylesheet" href="https://fonts.googleapis.com/css2?family=Alfa+Slab+One&family=Poiret+One&family=Roboto+Condensed:wght@700&display=swap">
<style>
  :root {
    --paper: #ffffff;
    --ink: #111111;
    --back: #0c0c0c;
    --back-soft: #1e1e1e;
    --title-red: #b3161c;
    --frame: #7a7a7a;
    --art-light: #f3eeee;
    --art-dark: #c9c9c9;
  }
  * { margin: 0; padding: 0; box-sizing: border-box; }
  html, body { width: 1200px; height: 1048px; overflow: hidden; background: var(--paper); }
  .canvas { position: relative; width: 1200px; height: 1048px; background: var(--paper); }

  .back-cover {
    position: absolute; left: 172px; top: 214px; width: 430px; height: 622px;
    background: radial-gradient(ellipse at 70% 15%, var(--back-soft), var(--back) 60%);
  }
  .synopsis-placeholder {
    position: absolute; left: 142px; top: 78px;
    font-family: "Poiret One", sans-serif; font-size: 16px; letter-spacing: 0.5px;
    color: var(--paper);
  }

  .spine-author {
    position: absolute; left: 591px; top: 262px;
    writing-mode: vertical-rl;
    font-family: "Poiret One", sans-serif; font-size: 12px; letter-spacing: 0.3px;
    color: var(--ink);
    background: var(--paper); padding: 2px 1px;
  }
  .spine-title {
    position: absolute; left: 588px; top: 630px;
    writing-mode: vertical-rl; transform: rotate(180deg);
    font-family: "Roboto Condensed", sans-serif; font-weight: 700; font-size: 14px;
    color: var(--paper);
  }

  .front-cover {
    position: absolute; left: 613px; top: 214px; width: 415px; height: 622px;
    border: 1px dashed var(--frame);
    background: var(--paper);
    overflow: hidden;
  }
  .cover-art {
    position: absolute; left: 180px; top: 180px; width: 234px; height: 441px;
  }
  .cover-author {
    position: absolute; right: 26px; top: 46px;
    font-family: "Poiret One", sans-serif; font-size: 17px; letter-spacing: 0.3px;
    color: var(--ink);
  }
  .cover-title {
    position: absolute; left: 45px; top: 30px;
    font-family: "Alfa Slab One", serif; font-size: 66px; line-height: 75px;
    color: var(--title-red);
  }
  .cover-title span { display: block; }
</style>
</head>
<body>
<div class="canvas">
  <section class="back-cover">
    <p class="synopsis-placeholder">Place for synopsis</p>
  </section>

  <div class="spine-author">ELENA VARDOS</div>
  <div class="spine-title">Una linterna en el muelle</div>

  <section class="front-cover">
    <svg class="cover-art" role="img" aria-label="Ilustración: árbol de hojas negras con manzanas rojas que crece de una torre de ajedrez, otras piezas y un tablero sobre el césped con huellas de pasos" viewBox="0 0 234 441" preserveAspectRatio="none">
      <defs>
        <linearGradient id="artTone" x1="0" y1="0" x2="0" y2="1">
          <stop offset="0" stop-color="var(--art-light)"/>
          <stop offset="1" stop-color="var(--art-dark)"/>
        </linearGradient>
      </defs>
      <rect width="234" height="441" fill="url(#artTone)"/>
    </svg>
    <p class="cover-author">ELENA VARDOS</p>
    <h1 class="cover-title">
      <span>Una</span>
      <span>linterna</span>
      <span>en</span>
      <span>el</span>
      <span>muelle</span>
    </h1>
  </section>
</div>
</body>
</html>
```